Out of School Care Business Needs Design for Indoor Pull-Up Banner & Outdoor Footpath Sign

We provide childcare and fun activities for kids aged between 5 years old and 14 years old. Service is based within local schools. Banner will be ...

Industry/Entity Type

Business

```html
<!DOCTYPE html>
<html lang="en">
<head>
<meta charset="utf-8">
<title>Joy Den – Pull-Up Banner</title>
<link href="https://fonts.googleapis.com/css2?family=Francois+One&family=Roboto:wght@400;500&display=swap" rel="stylesheet">
<style>
  :root {
    --page: #d9d9da;
    --ink: #1d1d1f;
    --yellow: #fff200;
    --pink: #ec008c;
    --cyan: #00aeef;
    --white: #ffffff;
  }
  * { box-sizing: border-box; margin: 0; padding: 0; }
  html, body { width: 1200px; height: 872px; overflow: hidden; }
  body { background: var(--page); font-family: "Roboto", sans-serif; }
  .banner {
    position: absolute; left: 445px; top: 16px;
    width: 310px; height: 840px;
    background: var(--ink);
    box-shadow: 0 10px 30px rgba(0,0,0,.25);
    overflow: hidden;
  }
  .banner-art { position: absolute; inset: 0; }
  .brand {
    position: absolute; top: 30px; left: 0; width: 100%;
    display: flex; align-items: center; justify-content: center; gap: 10px;
  }
  .brand-dot { width: 34px; height: 34px; border-radius: 50%; background: var(--pink); }
  .brand-name {
    font-family: "Francois One", sans-serif; font-size: 34px;
    color: var(--yellow); letter-spacing: .5px; text-transform: uppercase;
  }
  .headline {
    position: absolute; top: 128px; width: 100%; text-align: center;
    font-family: "Francois One", sans-serif; font-size: 70px; line-height: 1;
    color: var(--yellow);
  }
  .tagline {
    position: absolute; top: 208px; width: 100%; text-align: center;
    font-family: "Francois One", sans-serif; font-size: 28px; color: var(--white);
  }
  .services {
    position: absolute; top: 258px; left: 36px; right: 26px;
    list-style: none; display: flex; flex-direction: column; gap: 5px;
  }
  .service {
    height: 26px; border-radius: 8px; padding-left: 14px;
    font-size: 15px; line-height: 26px; color: var(--ink);
  }
  .service--pink { background: var(--pink); }
  .service--cyan { background: var(--cyan); }
  .service--yellow { background: var(--yellow); }
  .web {
    position: absolute; top: 778px; left: 40px;
    display: flex; align-items: center; gap: 12px;
    font-size: 21px; color: var(--white); letter-spacing: .5px;
  }
</style>
</head>
<body>
  <section class="banner">
    <svg class="banner-art" width="310" height="840" viewBox="0 0 310 840">
      <defs>
        <linearGradient id="kidsTone" x1="0" y1="0" x2="1" y2="1">
          <stop offset="0" stop-color="#c9a78b"/>
          <stop offset=".45" stop-color="#d8464f"/>
          <stop offset=".75" stop-color="#3f74b8"/>
          <stop offset="1" stop-color="#6c7f4a"/>
        </linearGradient>
        <linearGradient id="climbTone" x1="0" y1="0" x2="0" y2="1">
          <stop offset="0" stop-color="#8fa2b8"/><stop offset="1" stop-color="#5a4a52"/>
        </linearGradient>
        <linearGradient id="poolTone" x1="0" y1="0" x2="0" y2="1">
          <stop offset="0" stop-color="#7aa96a"/><stop offset="1" stop-color="#4cb6e0"/>
        </linearGradient>
        <linearGradient id="playTone" x1="0" y1="0" x2="0" y2="1">
          <stop offset="0" stop-color="#a7c0d8"/><stop offset="1" stop-color="#6e6a62"/>
        </linearGradient>
      </defs>
      <rect class="group-photo" role="img" aria-label="Photo of a group of cheerful school children in a classroom"
            x="0" y="330" width="310" height="340" fill="url(#kidsTone)"/>
      <path d="M0,330 L310,330 L310,352 Q160,425 0,360 Z" fill="var(--ink)"/>
      <path d="M120,392 Q220,400 310,352" fill="none" stroke="var(--cyan)" stroke-width="8"/>
      <path d="M0,656 Q130,590 310,706 L310,840 L0,840 Z" fill="var(--ink)"/>
      <path d="M0,656 Q130,590 310,706" fill="none" stroke="var(--pink)" stroke-width="10"/>
      <circle role="img" aria-label="Photo of children climbing" cx="58" cy="730" r="40" fill="url(#climbTone)" stroke="var(--pink)" stroke-width="6"/>
      <circle role="img" aria-label="Photo of children playing in a pool" cx="152" cy="718" r="40" fill="url(#poolTone)" stroke="var(--cyan)" stroke-width="6"/>
      <circle role="img" aria-label="Photo of children playing outdoor games" cx="246" cy="736" r="40" fill="url(#playTone)" stroke="var(--yellow)" stroke-width="6"/>
    </svg>

    <div class="brand">
      <span class="brand-dot"></span>
      <span class="brand-name">Joy Den</span>
    </div>
    <h1 class="headline">Joy Den</h1>
    <p class="tagline">Letting Kids Be Kids</p>
    <ul class="services">
      <li class="service service--pink">Before and after School Care</li>
      <li class="service service--cyan">School Holiday Programmes</li>
      <li class="service service--yellow">Make Your School Joy Den Cool</li>
    </ul>
    <div class="web">
      <svg width="18" height="18" viewBox="0 0 18 18" fill="none" stroke="#fff" stroke-width="1.3">
        <circle cx="9" cy="9" r="7.5"/><ellipse cx="9" cy="9" rx="3.2" ry="7.5"/>
        <line x1="1.5" y1="9" x2="16.5" y2="9"/><line x1="2.8" y1="5" x2="15.2" y2="5"/><line x1="2.8" y1="13" x2="15.2" y2="13"/>
      </svg>
      <span>joyden.co.nz</span>
    </div>
  </section>
</body>
</html>
```